New Upscale Product Line Package Design for dog chew company

Our brand is launching a new upscale product line that will have 5 new products variations. You will have to design 5 new packages

Please see document copy of wellness bags for the description of the 5 bags.

Our current packages are the orange ones, attached.

- The font stays the same
- All text is bilingual in english and french. In the document you see a < / > that is to separate French from English in the document. It can be used on the bag but it doesn’t have to, for example French can be on a line English on another line or tag etc.
- A ribbon is added to the packages with the name: Velvet Line / Gamme Velours, for the 5 packages
- Barcodes will be supplied once the design is chosen
- For dogs sizes removed
- Caution removed, replaced by information given for the back on the wellness bag document
-About us/Qui sommes nous removed and replaced by the new text on the wellness bag document
- This information stays the same: nutritional value, Made in, crunchy puff recipe
- Then individual changes, please see documents
- Example of what is removed on bag in image uploaded

the fonts are AmericusSansAged, Luckiest Guy and Neutra
- you can take an example of the bags designed by AI as an idea. We want the bags to feel luxurious.

Low design quality

Dog Owners

Dog chew business

• All the information on the Wellness bag document, all the information must be in english and french

```html
<!DOCTYPE html>
<html lang="en">
<head>
<meta charset="utf-8">
<title>Calm Yak – Velvet Line Pouch Label</title>
<link rel="stylesheet" href="https://fonts.googleapis.com/css2?family=Lato:wght@400&family=Playfair+Display:wght@700;900&family=Raleway:wght@400;500&display=swap">
<style>
  :root {
    --page-bg: #fdf3fa;
    --label-pink: #f6cbee;
    --cocoa: #76544f;
    --teal-ink: #1d4d4d;
    --dieline-blue: #2aa6e0;
    --window-light: #b8b8ba;
    --window-dark: #5c5c5e;
  }
  html, body {
    margin: 0;
    width: 1200px;
    height: 1200px;
    overflow: hidden;
    background: var(--page-bg);
  }
  .canvas {
    position: relative;
    width: 1200px;
    height: 1200px;
  }
  .pouch-label {
    position: absolute;
    left: 228px;
    top: 70px;
    width: 745px;
    height: 1060px;
  }
  .label-face { fill: var(--label-pink); }
  .dieline { fill: none; stroke: var(--dieline-blue); stroke-width: 1.6; }
  .dieline-dashed { stroke-dasharray: 8 6; }
  .dieline-text { font-family: Arial, Helvetica, sans-serif; font-size: 19px; fill: var(--dieline-blue); }
  .line-tag { font-family: "Raleway", sans-serif; font-weight: 500; font-size: 33px; fill: var(--teal-ink); letter-spacing: 0.5px; }
  .product-name { font-family: "Playfair Display", serif; font-weight: 900; font-size: 112px; fill: var(--cocoa); letter-spacing: 1px; }
  .product-name-fr { font-family: "Playfair Display", serif; font-weight: 900; font-size: 64px; fill: var(--cocoa); }
  .claim { font-family: "Playfair Display", serif; font-weight: 700; font-size: 38px; fill: var(--cocoa); letter-spacing: 1px; }
  .flavour { font-family: "Playfair Display", serif; font-weight: 700; font-size: 44px; fill: var(--cocoa); letter-spacing: 1px; }
  .net-weight { font-family: "Lato", sans-serif; font-size: 42px; fill: var(--cocoa); }
  .rule { stroke: var(--cocoa); stroke-width: 2; }
</style>
</head>
<body>
<main class="canvas">
  <svg class="pouch-label" viewBox="0 0 766 1090" xmlns="http://www.w3.org/2000/svg">
    <defs>
      <linearGradient id="window-shade" x1="0" x2="1" y1="0" y2="0">
        <stop offset="0" stop-color="var(--window-light)"/>
        <stop offset="1" stop-color="var(--window-dark)"/>
      </linearGradient>
      <radialGradient id="flower-tones" cx="0.5" cy="0.45" r="0.6">
        <stop offset="0" stop-color="#f7f2dc"/>
        <stop offset="0.6" stop-color="#e9efd8" stop-opacity="0.8"/>
        <stop offset="1" stop-color="#b9cf9c" stop-opacity="0"/>
      </radialGradient>
    </defs>

    <rect class="label-face" x="0" y="0" width="766" height="1090" rx="14"/>

    <!-- dieline marks -->
    <path class="dieline" d="M14 0 Q0 0 0 14 V1076 Q0 1090 14 1090 H752 Q766 1090 766 1076 V14 Q766 0 752 0"/>
    <path class="dieline dieline-dashed" d="M28 0 V1065 H740 V0"/>
    <path class="dieline" d="M0 100 L14 106 L0 112"/>
    <path class="dieline" d="M766 100 L752 106 L766 112"/>
    <line class="dieline" x1="385" y1="0" x2="385" y2="36"/>
    <text class="dieline-text" x="386" y="26">6mm</text>
    <path class="dieline" d="M332 52 H368 Q368 38 385 38 Q402 38 402 52 H436 Q452 52 452 68 Q452 84 436 84 H332 Q316 84 316 68 Q316 52 332 52 Z"/>
    <text class="dieline-text" x="384" y="75" text-anchor="middle">32x9mm</text>

    <!-- headings -->
    <text class="line-tag" x="385" y="155" text-anchor="middle">VELVET LINE | GAMME VELOURS</text>
    <text class="product-name" x="385" y="275" text-anchor="middle">CALM YAK</text>
    <text class="product-name-fr" x="392" y="352" text-anchor="middle">YAK CALME</text>

    <!-- product window -->
    <rect x="290" y="442" width="189" height="335" rx="94.5" fill="url(#window-shade)"/>
    <ellipse cx="393" cy="705" rx="150" ry="100" fill="url(#flower-tones)" role="img" aria-label="Illustration of chamomile flowers with stems and leaves"/>

    <!-- claims -->
    <text class="claim" x="385" y="848" text-anchor="middle">100% NATURAL</text>
    <line class="rule" x1="108" y1="878" x2="652" y2="878"/>
    <text class="flavour" x="385" y="937" text-anchor="middle">CHAMOMILE | CAMOMILLE</text>
    <line class="rule" x1="108" y1="968" x2="652" y2="968"/>
    <text class="net-weight" x="385" y="1027" text-anchor="middle">Min Net WT 160 g</text>
  </svg>
</main>
</body>
</html>
```